Banner Designs for Drone Defense Ad Campaign

Corvane is a security consulting and services company that offers a service called SkyMindful. SkyMindful helps our customers identify security risks from drones and develops comprehensive protection programs. We are looking for a designer to create a banner ad in three sizes for our campaign.
Target Market(s)
Our campaign is geared to the sports and entertainment industry, specifically large event venues and their security operation.
Industry/Entity Type
Security
Font styles to use
Other font styles liked:
- Raleway
Requirements
Must have
- Banner Objective
The visual and textual content of the banner should prompt the viewer to quickly identify the service offered and the information that is available to download.
Banner Design
Logo: SkyMindful logo
Call to Action Button in Red: Get It Here (On Right or or Upper Right)
Title in Larger Font: Guide to UAS Risk Mitigation
Subtitle in smaller Font: 5 Steps to Develop Your Comprehensive UAS Defense Program
Background: Stadium with a drone flying in foreground
Font: Raleway
Banner Sizes
1 - 1200x670 pixels
2 - 1510x196 pixels
3 - 1200x628 pixels

```html
<!DOCTYPE html>
<html lang="en">
<head>
<meta charset="utf-8">
<title>SkyMindful – Guide to UAS Risk Mitigation banners</title>
<link href="https://fonts.googleapis.com/css2?family=Raleway:wght@300;400;500;700;800&display=swap" rel="stylesheet">
<style>
  :root {
    --board: #e1e1e1;
    --label: #b9b9b9;
    --navy: #06152e;
    --blue: #0d4f9a;
    --glow: #2f8fe0;
    --turf: #1f5a1c;
    --night: #020406;
    --red: #ec1c24;
    --white: #ffffff;
    --drone: #dfe3e8;
    --brand-blue: #4e9ae0;
  }
  * { margin: 0; padding: 0; box-sizing: border-box; }
  html, body { width: 1200px; height: 611px; overflow: hidden; }
  body {
    background: var(--board);
    font-family: "Raleway", sans-serif;
    position: relative;
  }
  .size-label {
    position: absolute;
    font-weight: 400;
    font-size: 21px;
    color: var(--label);
    letter-spacing: 0.3px;
  }
  .banner {
    position: absolute;
    overflow: hidden;
    box-shadow: 3px 4px 5px rgba(0,0,0,0.28);
    color: var(--white);
  }
  .stadium-scene {
    position: absolute; inset: 0;
    background:
      radial-gradient(ellipse 70% 45% at 50% 62%, rgba(47,143,224,0.55), transparent 70%),
      linear-gradient(to bottom, var(--navy) 0%, #0a2f63 40%, var(--blue) 62%, #0b2a45 74%, var(--turf) 84%, var(--night) 100%);
  }
  .banner--leaderboard .stadium-scene {
    background:
      radial-gradient(ellipse 50% 90% at 45% 45%, rgba(47,143,224,0.5), transparent 70%),
      linear-gradient(to bottom, #030a18 0%, #0a2a5a 45%, #0b2d52 72%, var(--turf) 88%, var(--night) 100%);
  }
  .drone-photo {
    position: absolute;
    border-radius: 40% 40% 30% 30%;
    background: radial-gradient(ellipse at 50% 45%, var(--white) 0%, var(--drone) 45%, rgba(223,227,232,0) 72%);
  }
  .cta {
    position: absolute;
    background: var(--red);
    color: var(--white);
    font-weight: 800;
    display: flex; align-items: center; justify-content: center;
    text-transform: uppercase;
    letter-spacing: -0.1px;
  }
  .brand {
    position: absolute;
    display: flex; align-items: center; gap: 4px;
    font-weight: 500;
    color: var(--white);
  }
  .brand-dot { border-radius: 50%; background: var(--brand-blue); flex: none; }
  .title { position: absolute; white-space: nowrap; text-align: center; }
  .title-lead { color: var(--red); font-weight: 300; }
  .title-main { font-weight: 800; }
  .subtitle { position: absolute; text-align: center; font-weight: 500; white-space: nowrap; }

  /* 1510 x 196 */
  .banner--leaderboard { left: 80px; top: 95px; width: 638px; height: 82px; }
  .banner--leaderboard .title { left: 107px; top: 20px; width: 160px; line-height: 1.05; }
  .banner--leaderboard .title-lead { display: block; font-size: 14px; }
  .banner--leaderboard .title-main { display: block; font-size: 14.5px; margin-top: 2px; }
  .banner--leaderboard .drone-photo { left: 257px; top: 3px; width: 126px; height: 75px; }
  .banner--leaderboard .subtitle { left: 382px; top: 34px; width: 160px; font-size: 7.4px; line-height: 1.4; white-space: normal; }
  .banner--leaderboard .cta { left: 561px; top: 28px; width: 77px; height: 27px; font-size: 8.8px; }
  .banner--leaderboard .brand { left: 15px; top: 33px; font-size: 11px; }
  .banner--leaderboard .brand-dot { width: 7px; height: 7px; }

  /* 1200 x 670 */
  .banner--feature { left: 80px; top: 204px; width: 507px; height: 283px; }
  /* 1200 x 628 */
  .banner--social { left: 619px; top: 204px; width: 508px; height: 265px; }

  .banner--feature .title, .banner--social .title { left: 0; width: 100%; font-size: 26.5px; }
  .banner--feature .title { top: 30px; }
  .banner--social .title { top: 23px; }
  .banner--feature .subtitle, .banner--social .subtitle { left: 0; width: 100%; font-size: 10px; }
  .banner--feature .subtitle { top: 66px; }
  .banner--social .subtitle { top: 59px; }
  .banner--feature .drone-photo { left: 132px; top: 92px; width: 247px; height: 133px; }
  .banner--social .drone-photo { left: 128px; top: 85px; width: 249px; height: 147px; }
  .banner--feature .cta { left: 422px; top: 128px; width: 85px; height: 27px; font-size: 8.8px; }
  .banner--social .cta { left: 423px; top: 119px; width: 85px; height: 27px; font-size: 8.8px; }
  .banner--feature .brand { left: 15px; top: 230px; font-size: 15px; }
  .banner--social .brand { left: 16px; top: 214px; font-size: 15px; }
  .banner--feature .brand-dot, .banner--social .brand-dot { width: 9px; height: 9px; }
</style>
</head>
<body>
  <div class="size-label" style="left:80px; top:48px;">1510 x 196</div>

  <section class="banner banner--leaderboard">
    <div class="stadium-scene" role="img" aria-label="Floodlit sports stadium at night with green pitch"></div>
    <div class="brand"><span class="brand-dot"></span>SkyMindful</div>
    <h1 class="title"><span class="title-lead">Guide to</span><span class="title-main">UAS Risk Mitigation</span></h1>
    <div class="drone-photo" role="img" aria-label="White quadcopter drone with camera flying in the foreground"></div>
    <p class="subtitle">5 Steps to Develop Your Comprehensive UAS Defense Program</p>
    <a class="cta">Get it here</a>
  </section>

  <section class="banner banner--feature">
    <div class="stadium-scene" role="img" aria-label="Floodlit sports stadium at night with green pitch"></div>
    <h1 class="title"><span class="title-lead">Guide to </span><span class="title-main">UAS Risk Mitigation</span></h1>
    <p class="subtitle">5 Steps to Develop Your Comprehensive UAS Defense Program</p>
    <div class="drone-photo" role="img" aria-label="White quadcopter drone with camera flying in the foreground"></div>
    <a class="cta">Get it here</a>
    <div class="brand"><span class="brand-dot"></span>SkyMindful</div>
  </section>

  <section class="banner banner--social">
    <div class="stadium-scene" role="img" aria-label="Floodlit sports stadium at night with green pitch"></div>
    <h1 class="title"><span class="title-lead">Guide to </span><span class="title-main">UAS Risk Mitigation</span></h1>
    <p class="subtitle">5 Steps to Develop Your Comprehensive UAS Defense Program</p>
    <div class="drone-photo" role="img" aria-label="White quadcopter drone with camera flying in the foreground"></div>
    <a class="cta">Get it here</a>
    <div class="brand"><span class="brand-dot"></span>SkyMindful</div>
  </section>

  <div class="size-label" style="left:75px; top:509px;">1200 x 670</div>
  <div class="size-label" style="left:614px; top:509px;">1200 x 628</div>
</body>
</html>
```